Vyntra Ad Design for Culinary Toursim Company

Looking for ad design for www.savorlanewalks.example to be used on VYNTRA traffic ads.

Below is one example of the

We are looking for vyntra ad design
Post: 1080x1080 with text,
Stories: 1080x1920 with text

Text should read
Food For Thought
CTA: Join our {CITY} Food Tour

Logo and optional photos are attached. You can edit the photos as you see fit.
Brand guidelines https://www.filevault.example/s/k3m9q2x7/Savor-Lane-Walks-Brand-Guidelines.docx

Logos https://www.filevault.example/f/r8t4w1z6/logos

Target Market(s)

United States Foodies ages 30-65

Industry/Entity Type

Tourism

Font styles to use
Other font styles liked:
• Avenir

Requirements
Must have
• High Design
Nice to have
• See Brand Guidelines
Should not have
• See Brand Guidelines

```html
<!DOCTYPE html>
<html lang="en">
<head>
<meta charset="utf-8">
<title>Savor Lane Walks – Food For Thought</title>
<link rel="stylesheet" href="https://fonts.googleapis.com/css2?family=Montserrat:wght@300;400;700;800&family=Roboto:wght@400;500&display=swap">
<style>
  :root {
    --blush: #ecc2b2;
    --blush-light: #f4cdbd;
    --crimson: #a80000;
    --crimson-deep: #8a0000;
    --ink: #0a0a0a;
    --white: #ffffff;
    --photo-dark: #2a1f19;
    --photo-warm: #7a5a3e;
  }
  html, body {
    margin: 0;
    padding: 0;
    width: 1200px;
    height: 1200px;
    overflow: hidden;
    background: var(--blush);
  }
  .canvas {
    width: 1200px;
    height: 1200px;
    overflow: hidden;
    position: relative;
  }
  .ad {
    position: absolute;
    top: 0;
    left: 0;
    width: 1080px;
    height: 1080px;
    transform: scale(1.1111111);
    transform-origin: 0 0;
    background: var(--blush);
    font-family: "Roboto", Arial, sans-serif;
  }
  .ad-shapes {
    position: absolute;
    inset: 0;
    width: 1080px;
    height: 1080px;
  }
  .brand {
    position: absolute;
    left: 62px;
    top: 92px;
    display: flex;
    align-items: center;
    gap: 12px;
    color: var(--white);
    font-family: "Montserrat", Arial, sans-serif;
    font-weight: 700;
    font-size: 26px;
    letter-spacing: 0.5px;
  }
  .brand-mark {
    width: 18px;
    height: 18px;
    background: var(--white);
  }
  .headline {
    position: absolute;
    left: 72px;
    top: 318px;
    margin: 0;
    color: var(--blush-light);
    font-family: "Montserrat", Arial, sans-serif;
    line-height: 1;
    z-index: 2;
  }
  .headline span { display: block; }
  .headline .light {
    font-weight: 300;
    font-size: 64px;
    letter-spacing: 3px;
    margin-bottom: 24px;
  }
  .headline .bold {
    font-weight: 800;
    font-size: 66px;
    letter-spacing: 0;
    margin-top: 0;
  }
  .cta {
    position: absolute;
    left: 71px;
    top: 603px;
    width: 262px;
    height: 86px;
    border: 2px solid var(--blush-light);
    display: flex;
    align-items: center;
    justify-content: center;
    text-align: center;
    color: var(--blush-light);
    font-weight: 500;
    font-size: 20px;
    line-height: 30px;
  }
  .web {
    position: absolute;
    left: 62px;
    top: 993px;
    display: flex;
    align-items: center;
    gap: 16px;
    color: var(--ink);
    font-size: 28px;
    letter-spacing: 0.3px;
  }
  .icon-circle {
    width: 46px;
    height: 46px;
    border-radius: 50%;
    background: var(--crimson);
    display: flex;
    align-items: center;
    justify-content: center;
  }
  .contact {
    position: absolute;
    right: 127px;
    top: 988px;
    text-align: right;
    color: var(--ink);
  }
  .contact-label {
    font-size: 20px;
    margin: 0 0 6px;
  }
  .contact-phone {
    font-size: 34px;
    font-weight: 500;
    margin: 0;
    letter-spacing: 0.5px;
  }
  .phone-icon {
    position: absolute;
    left: 965px;
    top: 992px;
    width: 56px;
    height: 56px;
  }
  .code {
    position: absolute;
    left: 1038px;
    top: 1046px;
    font-size: 11px;
    color: var(--ink);
  }
</style>
</head>
<body>
<div class="canvas">
  <div class="ad">
    <svg class="ad-shapes" viewBox="0 0 1080 1080" xmlns="http://www.w3.org/2000/svg">
      <defs>
        <linearGradient id="photoTone" x1="0" y1="0" x2="1" y2="1">
          <stop offset="0" stop-color="#4a3a2c"/>
          <stop offset="0.5" stop-color="#2a1f19"/>
          <stop offset="1" stop-color="#7a5a3e"/>
        </linearGradient>
        <clipPath id="photoClip">
          <path d="M795,155 L1080,318 L1080,690 L722,876 L462,706 L462,334 Z"/>
        </clipPath>
      </defs>

      <path class="accent-red" d="M865,182 L1080,60 L1080,335 Z" fill="var(--crimson)"/>
      <path class="panel-red" d="M0,190 L240,228 L490,330 L725,820 L505,945 Q472,962 440,946 L0,722 Z" fill="var(--crimson)"/>
      <path class="panel-black" d="M0,0 L632,0 L232,236 Q192,260 150,246 L0,190 Z" fill="var(--ink)"/>

      <path class="photo-shadow" d="M795,155 L1080,318 L1080,690 L722,876 L462,706 L462,334 Z"
            fill="none" stroke="var(--crimson-deep)" stroke-width="44" stroke-linejoin="round" transform="translate(-8,0)"/>
      <path class="photo-frame" d="M795,155 L1080,318 L1080,690 L722,876 L462,706 L462,334 Z"
            fill="var(--white)" stroke="var(--white)" stroke-width="20" stroke-linejoin="round"/>
      <g clip-path="url(#photoClip)">
        <rect class="photo" x="440" y="140" width="650" height="760" fill="url(#photoTone)"
              role="img" aria-label="Photo: a chef pouring sauce over a plated dish in a warm restaurant kitchen under pendant lamps, with fries and salad on the counter"/>
      </g>

      <circle cx="993" cy="71" r="5.5" fill="var(--ink)"/>
      <circle cx="1013" cy="71" r="5.5" fill="var(--ink)"/>
    </svg>

    <div class="brand"><span class="brand-mark"></span>Savor Lane Walks</div>

    <h1 class="headline">
      <span class="light">FOOD</span>
      <span class="light">FOR</span>
      <span class="bold">THOUGHT</span>
    </h1>

    <div class="cta">JOIN OUR MARSEILLE<br>FOOD TOUR</div>

    <div class="web">
      <span class="icon-circle">
        <svg width="24" height="24" viewBox="0 0 24 24" fill="none" stroke="#fff" stroke-width="2.6" stroke-linecap="round">
          <path d="M10 14a4 4 0 0 0 5.7 0l3-3a4 4 0 0 0-5.7-5.7l-1 1"/>
          <path d="M14 10a4 4 0 0 0-5.7 0l-3 3a4 4 0 0 0 5.7 5.7l1-1"/>
        </svg>
      </span>
      www.savorlanewalks.example
    </div>

    <div class="contact">
      <p class="contact-label">More Info Call Us:</p>
      <p class="contact-phone">+1 555-014-2297</p>
    </div>

    <svg class="phone-icon" viewBox="0 0 56 56" xmlns="http://www.w3.org/2000/svg">
      <path d="M10 14c2-3 5-4 7-2l4 6c1 2 0 3-1 4l-2 2c1 4 5 8 9 10l2-2c1-1 3-2 4-1l6 4c2 2 1 5-2 7-4 3-10 1-17-6S7 19 10 14Z" fill="var(--crimson)"/>
      <rect x="26" y="2" width="26" height="18" rx="7" fill="var(--crimson)"/>
      <path d="M32 19 L30 26 L38 19 Z" fill="var(--crimson)"/>
      <circle cx="33" cy="11" r="2" fill="#fff"/>
      <circle cx="39" cy="11" r="2" fill="#fff"/>
      <circle cx="45" cy="11" r="2" fill="#fff"/>
    </svg>

    <div class="code">C45</div>
  </div>
</div>
</body>
</html>
```